Stationery Design Project - Tax Professionals/Chartered Accountants

The name of our firm is “Penwick Group” and our slogan is “Bright Pathways”. You can also use the name "The Penwick Group" if it works better.

We are looking for a full stationery design: Letterhead, Business Card and With Compliments slip

We are looking for a bold, modern and clean/simple design that makes us stand out. We stand out as professionals in the industry and would like the stationery that our clients see to convey this image as well.

There is no colour preference.

We have used a "Lion" as our logo/symbol and that has received positive feedback from our clients; if you think the lion works then please incorporate the "lion".

If you think another symbol works then please submit this we are very open to ideas and would like to see designs that don't incorporate a lion as well.

We would like a corporate feel to this.

You could also incorporate the LG logo http://www.ledgerguildexample.com.au/Members/Marketing-your-practice/Logos but this is not a must.

WHO WE ARE:-
We are a Chartered Accounting firm who specialise in the delivery of taxation and strategic insolvency services. We also provide financial reporting services that help clients negotiate and compromise their debt or expenses such as rent with their landlords.

We work with Law Firms, other Accountants to deliver the best service for our clients.

Our clients come from varied backgrounds and are largely successful and established businesses and high net worth individuals looks for effective tax planning.

We are not the usual accounting firm and do not provide traditional tax return based services.
Updates

Reason: There are still designers who have signed on but not yet submitted designs and also adjustments to existing designs submitted. Extra time so designers are not rushed.

Target Market(s)

Corporate/ Independent successful businesses and individuals

Industry/Entity Type

Business

Requirements
Must have
• The letter must have the following phrase
“Liability limited by a scheme approved under Professional Standards Legislation”

The letter must also have the following business information:-
“The Penwick Group Pty Ltd atf
Principal - Colin T. Penwick
ABN: 47 215 708 362”

Plus Usual Address & Contact Details

We would also a logo or symbol that is representative of us. We like the idea of a lion but this is not set in stone and are very open to ideas.

```html
<!DOCTYPE html>
<html lang="en">
<head>
<meta charset="utf-8">
<title>The Penwick Group – Stationery</title>
<link rel="stylesheet" href="https://fonts.googleapis.com/css2?family=Open+Sans:wght@400;600;700&family=Questrial&display=swap">
<style>
:root{
  --stage:#383838;
  --paper:#ffffff;
  --brand:#c8102e;
  --brand-faint:#f6dfe3;
  --ink:#222222;
  --muted:#666666;
  --rule:#555555;
  --flap-grey:#6b6b6b;
  --label:#f2f2f2;
}
*{box-sizing:border-box;margin:0;padding:0}
html,body{width:1200px;height:539px;overflow:hidden}
body{background:var(--stage);font-family:"Open Sans",Arial,sans-serif;color:var(--ink);position:relative}
.sheet{position:absolute;background:var(--paper);box-shadow:0 1px 3px rgba(0,0,0,.4);overflow:hidden}
.brand{position:absolute;display:flex;align-items:center;gap:4px;color:var(--brand);font-weight:700;white-space:nowrap}
.brand .dot{border-radius:50%;background:var(--brand);flex:none}
.brand.faint{color:var(--brand-faint)}
.brand.faint .dot{background:var(--brand-faint)}
.brand.stack{flex-direction:column}
.brand.stack-left{flex-direction:column;align-items:flex-start}
.brand.centered{left:0;right:0;justify-content:center}
.band{position:absolute;left:0;right:0;background:var(--brand);color:#fff;text-align:center}
.small{position:absolute;font-size:5px;line-height:1.45;color:var(--muted)}
.option-label{position:absolute;top:488px;font-family:"Questrial",sans-serif;font-size:28px;color:var(--label);letter-spacing:.5px}

/* letterhead */
.letterhead{left:53px;top:53px;width:330px;height:427px}
.letterhead .band{bottom:0;height:23px;font-size:5px;padding-top:4px;line-height:1.7}
.letterhead-mark{top:142px;font-size:15px;gap:34px}

/* fax */
.fax{left:405px;top:53px;width:330px;height:427px}
.fax .band{bottom:0;height:18px;font-size:6px;line-height:18px}
.fax-title{position:absolute;left:33px;top:66px;font-size:17px;font-weight:400;color:#111}
.fax-field{position:absolute;height:14px;border-bottom:1px solid var(--rule);font-size:5px;padding-top:4px}
.fax-checks{position:absolute;left:32px;top:172px;display:flex;gap:14px;font-size:5px;align-items:center}
.fax-checks span{display:flex;align-items:center;gap:5px}
.fax-checks i{display:inline-block;width:7px;height:7px;border:1px solid #444}

/* envelopes */
.envelope{width:263px;height:143px}
.envelope .flap{position:absolute;left:0;right:0;top:0;height:30px;border-radius:0 0 60% 60%/0 0 40% 40%}
.envelope .base-rule{position:absolute;left:0;right:0;bottom:14px;border-top:1px solid #999}
.envelope .band{bottom:0;height:10px;font-size:5px;line-height:10px;text-align:left;padding-left:8px}
.env-red{left:765px;top:73px}
.env-red .flap{background:var(--brand)}
.env-grey{left:866px;top:165px}
.env-grey .flap{background:var(--flap-grey)}
.env-white{left:765px;top:230px}
.env-white .flap{border:1px solid #bbb;border-top:none;background:var(--paper)}
.env-grey .band,.env-white .band{text-align:right;padding-right:8px}

/* cards */
.card{width:133px;height:77px;border-radius:7px}
.card-front{left:762px;top:400px}
.card-back{left:924px;top:402px}
.card-front .band{bottom:0;height:26px;font-size:3.6px;line-height:1.6;padding-top:3px}
.partner-badge{position:absolute;right:8px;top:5px;width:24px;height:12px;background:#e9e9e9;border-radius:2px}
</style>
</head>
<body>

<!-- Letterhead -->
<section class="sheet letterhead" aria-label="Letterhead">
  <div class="brand stack-left" style="left:10px;top:7px;font-size:5px;gap:3px"><span class="dot" style="width:26px;height:26px;margin-left:17px"></span>The Penwick Group Pty Ltd atf</div>
  <p class="small" style="left:10px;top:46px">Liability limited by a scheme approved under Professional Standards Legislation</p>
  <p class="small" style="right:11px;top:19px;text-align:right">Principal - Colin T. Penwick<br>ABN: 47 215 708 362</p>
  <div class="brand faint stack centered letterhead-mark"><span class="dot" style="width:100px;height:100px"></span>The Penwick Group Pty Ltd atf</div>
  <div class="band">&#9742; 123-456-7890 &nbsp; &#9113; 123-456-7890 &nbsp; &#9993; name@website.com &nbsp; www.website.com<br>Street name, City, State, zip code</div>
</section>
<div class="option-label" style="left:157px">option 1</div>

<!-- Fax -->
<section class="sheet fax" aria-label="Fax cover sheet">
  <div class="brand stack" style="left:30px;top:7px;font-size:5px;gap:3px"><span class="dot" style="width:26px;height:26px"></span>The Penwick Group Pty Ltd atf</div>
  <p class="small" style="left:255px;top:14px;border-left:1px solid #bbb;padding-left:5px">Street name<br>City, State, zip code<br><span style="color:var(--brand)">&#9742;</span> 123-456-7890<br><span style="color:var(--brand)">&#9113;</span> 123-456-7890<br><span style="color:var(--brand)">&#9993;</span> name@website.com</p>
  <h1 class="fax-title">FAX</h1>
  <div class="fax-field" style="left:32px;top:94px;width:152px">To :</div>
  <div class="fax-field" style="left:186px;top:94px;width:103px">From :</div>
  <div class="fax-field" style="left:32px;top:110px;width:152px">Fax :</div>
  <div class="fax-field" style="left:186px;top:110px;width:103px">Pages :</div>
  <div class="fax-field" style="left:32px;top:125px;width:152px">Phone :</div>
  <div class="fax-field" style="left:186px;top:125px;width:103px">Date :</div>
  <div class="fax-field" style="left:32px;top:141px;width:152px">Re :</div>
  <div class="fax-field" style="left:186px;top:141px;width:103px">CC :</div>
  <div class="fax-checks">
    <span><i></i>Urgent</span><span><i></i>For Review</span><span><i></i>Please Comment</span><span><i></i>Please Reply</span><span><i></i>Please Recycle</span>
  </div>
  <div class="brand faint stack" style="left:234px;top:346px;font-size:5px;gap:3px"><span class="dot" style="width:30px;height:30px"></span>The Penwick Group Pty Ltd atf</div>
  <div class="band">www.website.com</div>
</section>
<div class="option-label" style="left:521px">option 2</div>

<!-- Envelopes -->
<section class="sheet envelope env-red" aria-label="Envelope with red flap">
  <div class="flap"></div>
  <div class="brand stack" style="left:112px;top:3px;font-size:3.5px;color:#fff;gap:1px"><span class="dot" style="width:13px;height:13px;background:#fff"></span>The Penwick Group Pty Ltd atf</div>
  <div class="brand stack-left" style="left:5px;top:33px;font-size:4.5px;gap:2px"><span class="dot" style="width:20px;height:20px;margin-left:18px"></span>The Penwick Group Pty Ltd atf</div>
  <div class="base-rule"></div>
  <div class="band">www.website.com</div>
</section>

<section class="sheet envelope env-grey" aria-label="Envelope with grey flap">
  <div class="flap"></div>
  <div class="brand stack" style="left:112px;top:3px;font-size:3.5px;color:#fff;gap:1px"><span class="dot" style="width:13px;height:13px;background:#fff"></span>The Penwick Group Pty Ltd atf</div>
  <div class="brand faint stack" style="left:172px;top:74px;font-size:4.5px;gap:2px"><span class="dot" style="width:28px;height:28px"></span>The Penwick Group Pty Ltd atf</div>
  <div class="base-rule"></div>
  <div class="band">www.website.com</div>
</section>

<section class="sheet envelope env-white" aria-label="White envelope">
  <div class="flap"></div>
  <div class="brand stack" style="left:112px;top:4px;font-size:3.5px;gap:1px"><span class="dot" style="width:13px;height:13px"></span>The Penwick Group Pty Ltd atf</div>
  <div class="brand stack-left" style="left:5px;top:34px;font-size:4.5px;gap:2px"><span class="dot" style="width:20px;height:20px;margin-left:18px"></span>The Penwick Group Pty Ltd atf</div>
  <div class="brand faint stack" style="left:170px;top:73px;font-size:4.5px;gap:2px"><span class="dot" style="width:28px;height:28px"></span>The Penwick Group Pty Ltd atf</div>
  <div class="base-rule"></div>
  <div class="band">www.website.com</div>
</section>

<!-- Business cards -->
<section class="sheet card card-front" aria-label="Business card front">
  <div class="brand stack" style="left:34px;top:5px;font-size:4px;gap:2px"><span class="dot" style="width:20px;height:20px"></span>The Penwick Group Pty Ltd atf</div>
  <div class="partner-badge" role="img" aria-label="Professional body badge"></div>
  <p class="small" style="left:0;right:0;top:37px;text-align:center;font-size:3.6px;color:var(--ink)">Colin T. Penwick, Principal<br><span style="color:var(--muted)">Bright Pathways</span></p>
  <div class="band" style="border-radius:0 0 7px 7px">&#9742; 123-456-7890 &nbsp;|&nbsp; &#9993; name@website.com<br>&#9113; 123-456-7890 &nbsp;|&nbsp; www.website.com<br>Street name, City, State, zip code</div>
</section>

<section class="sheet card card-back" aria-label="Business card back">
  <div class="brand faint stack centered" style="top:9px;font-size:5.5px;gap:4px;color:var(--brand)"><span class="dot" style="width:32px;height:32px;background:var(--brand)"></span>The Penwick Group Pty Ltd atf</div>
  <p class="small" style="left:0;right:0;top:63px;text-align:center;font-size:4px">www.website.com</p>
</section>

</body>
</html>
```